Need a stunning looking Business Card Design for my Telecom Business, Wow FACTOR!

I deal with high level IT Directors , and Contractors.
I need to impress them with a sleek , professional and unique business card.
Im thinking options as far as rounded edges, plastic , or even metal card or die cut on a corner.
Whatever looks better and leave an unforgettable first impression.
im looking for the wow factor.
Front should have the basics info (attached on the picture of current business card)
i would like to add picture of myself somewhere
Back side
should have logo and maybe some pictures or past projects, you can download from my website ( www.lumvexholdings.com)

```html
<!DOCTYPE html>
<html lang="en">
<head>
<meta charset="utf-8">
<title>Lumvex Holdings — Business Card</title>
<link href="https://fonts.googleapis.com/css2?family=Saira:wght@400;500;700;800&display=swap" rel="stylesheet">
<style>
  :root {
    --stage: #2a2a2c;
    --card-black: #050505;
    --card-white: #ffffff;
    --card-grey: #ececec;
    --navy: #16275e;
    --navy-deep: #0f1c48;
    --accent-blue: #2f8fe0;
    --sky: #4fb3ea;
    --lime: #8cc63f;
    --gold: #e6c21c;
    --text-light: #ffffff;
  }
  * { box-sizing: border-box; margin: 0; padding: 0; }
  html, body {
    width: 1200px; height: 900px; overflow: hidden;
    background: var(--stage);
    font-family: "Saira", sans-serif;
  }
  .stage { position: relative; width: 1200px; height: 900px; }

  .card {
    position: absolute;
    border-radius: 28px;
    overflow: hidden;
    box-shadow: 0 18px 40px rgba(0,0,0,.55);
  }

  /* Back side */
  .card-back {
    left: 110px; top: 50px;
    width: 560px; height: 320px;
    background: var(--card-black);
    display: flex; align-items: center; justify-content: center;
  }
  .brand { display: flex; align-items: center; gap: 14px; }
  .brand-mark { width: 22px; height: 22px; }
  .brand-name {
    font-weight: 500;
    letter-spacing: .12em;
    line-height: 1.05;
    text-transform: uppercase;
  }
  .brand-name small { display: block; font-size: .42em; letter-spacing: .5em; }
  .card-back .brand-name { color: var(--text-light); font-size: 34px; }
  .card-back .brand-mark { background: var(--text-light); }

  /* Front side */
  .card-front {
    left: 400px; top: 430px;
    width: 700px; height: 400px;
    background: linear-gradient(100deg, var(--card-white) 0%, var(--card-grey) 55%, var(--card-white) 100%);
  }
  .wave { position: absolute; inset: 0; width: 700px; height: 400px; }

  .card-front .brand { position: absolute; left: 46px; top: 110px; }
  .card-front .brand-name { color: var(--navy); font-size: 36px; }
  .card-front .brand-mark { background: var(--navy); }

  .portrait-frame {
    position: absolute; left: 470px; top: 20px;
    width: 190px; height: 150px;
    border-radius: 22px; padding: 4px;
    background: linear-gradient(135deg, var(--lime), var(--gold));
  }
  .portrait {
    width: 100%; height: 100%; border-radius: 18px;
    background: linear-gradient(160deg, #e9c9a4 0%, #c6a488 45%, #8c8f96 100%);
  }

  .identity { position: absolute; right: 40px; top: 178px; text-align: right; }
  .person-name {
    color: var(--navy); font-weight: 800; font-size: 24px;
    letter-spacing: .06em; text-transform: uppercase; line-height: 1.05;
  }
  .person-role { color: var(--lime); font-size: 15px; font-weight: 500; letter-spacing: .04em; line-height: 1.3; }

  .contact-list { position: absolute; list-style: none; color: var(--text-light); font-size: 13px; }
  .contact-list li { display: flex; align-items: center; gap: 8px; height: 20px; white-space: nowrap; }
  .contact-list svg { width: 14px; height: 14px; flex: none; fill: var(--sky); }
  .contact-phones { left: 180px; top: 310px; }
  .contact-web { left: 372px; top: 296px; }
</style>
</head>
<body>
<main class="stage">

  <section class="card card-back" aria-label="Card back">
    <div class="brand">
      <span class="brand-mark"></span>
      <p class="brand-name">Lumvex<small>Holdings</small></p>
    </div>
  </section>

  <section class="card card-front" aria-label="Card front">
    <svg class="wave" viewBox="0 0 700 400" aria-hidden="true">
      <path d="M52,400 C84,300 200,272 420,262 C560,256 640,256 700,240 L700,400 Z" fill="var(--accent-blue)"/>
      <path d="M64,400 C96,308 210,282 424,272 C562,266 642,266 700,252 L700,400 Z" fill="var(--navy)"/>
      <path d="M64,400 C96,308 210,282 424,272 C562,266 642,266 700,252 L700,270 C640,286 560,288 430,292 C240,300 120,334 96,400 Z" fill="var(--navy-deep)" opacity=".5"/>
    </svg>

    <div class="brand">
      <span class="brand-mark"></span>
      <p class="brand-name">Lumvex<small>Holdings</small></p>
    </div>

    <div class="portrait-frame">
      <div class="portrait" role="img" aria-label="Portrait photo of the operations manager"></div>
    </div>

    <div class="identity">
      <p class="person-name">Kenji Arata</p>
      <p class="person-role">Operations Manager</p>
    </div>

    <ul class="contact-list contact-phones">
      <li><svg viewBox="0 0 16 16"><path d="M3 2h3l1 3-2 1a9 9 0 0 0 5 5l1-2 3 1v3a1 1 0 0 1-1 1A13 13 0 0 1 2 3a1 1 0 0 1 1-1z"/></svg>(305) 555-0148 Miami</li>
      <li><svg viewBox="0 0 16 16"><path d="M3 2h3l1 3-2 1a9 9 0 0 0 5 5l1-2 3 1v3a1 1 0 0 1-1 1A13 13 0 0 1 2 3a1 1 0 0 1 1-1z"/></svg>(954) 555-0172 Broward</li>
      <li><svg viewBox="0 0 16 16"><path d="M3 2h3l1 3-2 1a9 9 0 0 0 5 5l1-2 3 1v3a1 1 0 0 1-1 1A13 13 0 0 1 2 3a1 1 0 0 1 1-1z"/></svg>(561) 555-0193 Palm Beach</li>
      <li><svg viewBox="0 0 16 16"><path d="M1 4h14v9H1z M1 4l7 5 7-5" stroke="var(--navy)" stroke-width="1"/></svg>info@lumvexholdings.com</li>
    </ul>

    <ul class="contact-list contact-web">
      <li><svg viewBox="0 0 16 16"><circle cx="8" cy="8" r="7"/><path d="M1 8h14M8 1c3 3 3 11 0 14M8 1c-3 3-3 11 0 14" stroke="var(--navy)" fill="none"/></svg>www.lumvexholdings.com</li>
      <li><svg viewBox="0 0 16 16"><path d="M8 1a5 5 0 0 1 5 5c0 4-5 9-5 9S3 10 3 6a5 5 0 0 1 5-5zm0 3a2 2 0 1 0 0 4 2 2 0 0 0 0-4z"/></svg>Offices in Miami, Broward and Palm Beach</li>
    </ul>
  </section>

</main>
</body>
</html>
```